business cards and stationary for landscaping company
Seven Hollows Lawn and Landscaping
business cards and stationary for landscaping company - Home and Garden
Creative Brief
Use specific fonts
Feel free to change fonts
Simple
Desmond Kuparik
2817 Mellard Rd. Fernwick LV K2p4v8
Desmond@kuparik-mail.example
7HollowsLL.example
On the front of the cards we would like it to be simple and clean with just the logo. Personal name and number. We need it in a format so we can change all of the contact information for the other owners of the company so make sure we will be able to do that with the design submissions. We are not looking for anything to crazy in terms of the design so pleas NO see thru cards that iv seen on here before or anything that will cost extra to have printed. We would like to see the face of the cards on White Green and Black there are three owners so we would like each to have a different card face. I will attach some samples of the front of the cards and colors we liked. We don't need an address on the card We would also like the same design as business card in a larger format to put on postcards plus maybe the addition of a picture of some of our work we have done. i will attach some pictures as well for the postcards.
On the Back of the cards we would like to include our services and once more all our contact information including name number email and website domain Landscaping - Patio Design and Insulation and Repair - Walkway Design and Insulation - Garden and Driveway Edging - & More Property Maintenance - Lawn Care - Brush Cutting - Yard Cleanup & More Please remember to make the text able to be edited. so we are able to make changes if necessary.

```html
<!DOCTYPE html>
<html lang="en">
<head>
<meta charset="utf-8">
<title>Seven Hollows Lawn and Landscaping – Business Cards</title>
<link href="https://fonts.googleapis.com/css2?family=PT+Serif:wght@400;700&display=swap" rel="stylesheet">
<style>
  :root {
    --backdrop: #1f1f1f;
    --green: #1f8a3c;
    --green-deep: #16702f;
    --green-dark: #0f5a25;
    --white: #ffffff;
    --paper: #f4f4f2;
    --ink: #3a3a3a;
    --ink-soft: #555555;
  }
  * { margin: 0; padding: 0; box-sizing: border-box; }
  html, body { width: 1200px; height: 871px; overflow: hidden; background: var(--backdrop); }
  body { position: relative; font-family: "PT Serif", Georgia, serif; }

  .card {
    position: absolute;
    width: 620px;
    height: 360px;
    border-radius: 4px;
    box-shadow: 0 14px 30px rgba(0,0,0,0.55);
    overflow: hidden;
  }

  /* Back of card */
  .card-back {
    left: 100px; top: 110px;
    background: linear-gradient(135deg, var(--green) 0%, var(--green-deep) 60%, var(--green-dark) 100%);
    color: var(--white);
  }
  .services {
    position: absolute;
    left: 90px; top: 70px;
    display: flex;
    gap: 24px;
  }
  .service-group { font-size: 13px; line-height: 1.6; white-space: nowrap; }
  .service-group h3 { font-size: 16px; font-weight: 700; margin-bottom: 6px; }
  .service-group.landscaping { text-align: right; padding-right: 24px; border-right: 1px solid rgba(255,255,255,0.7); }
  .service-group ul { list-style: none; }

  /* Front of card */
  .card-front {
    left: 480px; top: 420px;
    background: linear-gradient(160deg, var(--white) 0%, var(--paper) 100%);
    color: var(--ink);
  }
  .brand {
    position: absolute;
    left: 175px; top: 58px;
    display: flex;
    align-items: flex-start;
    gap: 14px;
  }
  .brand-square { width: 46px; height: 46px; background: var(--green); margin-top: 4px; }
  .brand-name { color: var(--green); font-weight: 400; line-height: 1.05; white-space: nowrap; }
  .brand-name .main { display: block; font-size: 33px; letter-spacing: 0.5px; }
  .brand-name .sub { display: block; font-size: 17px; letter-spacing: 0.3px; }

  .name-band {
    position: absolute;
    left: 0; right: 0; top: 160px;
    height: 44px;
    background: linear-gradient(180deg, var(--green) 0%, var(--green-deep) 100%);
    border-top: 3px solid var(--white);
    box-shadow: 0 -4px 0 var(--green), 0 4px 0 var(--green);
  }
  .name-band .person {
    position: absolute; left: 0; right: 0; top: 9px;
    text-align: center; color: var(--white); font-size: 18px; letter-spacing: 0.5px;
  }
  .name-band .band-mark {
    position: absolute; right: 22px; top: -14px;
    width: 62px; height: 66px;
    background: var(--white);
    border: 3px solid var(--green);
  }
  .band-mark::after {
    content: ""; position: absolute; inset: 10px; background: var(--green);
  }

  .address {
    position: absolute; left: 0; right: 0; top: 236px;
    text-align: center; font-size: 13px; color: var(--ink-soft);
  }
  .contact {
    position: absolute; left: 0; right: 0; top: 262px;
    text-align: center; font-size: 12.5px; color: var(--ink-soft); white-space: nowrap;
  }
  .contact .label { color: var(--green); font-weight: 700; }
</style>
</head>
<body>

  <section class="card card-back" aria-label="Back of business card">
    <div class="services">
      <div class="service-group landscaping">
        <h3>Landscaping</h3>
        <ul>
          <li>Patio Design and Insulation and Repair</li>
          <li>Walkway Design and Insulation</li>
          <li>Garden and Driveway Edging</li>
          <li>&amp; More</li>
        </ul>
      </div>
      <div class="service-group maintenance">
        <h3>Property Maintenance</h3>
        <ul>
          <li>Lawn Care</li>
          <li>Brush Cutting</li>
          <li>Yard Cleanup</li>
          <li>&amp; More</li>
        </ul>
      </div>
    </div>
  </section>

  <section class="card card-front" aria-label="Front of business card">
    <div class="brand">
      <div class="brand-square"></div>
      <div class="brand-name">
        <span class="main">SEVEN HOLLOWS</span>
        <span class="sub">LAWN AND LANDSCAPING</span>
      </div>
    </div>

    <div class="name-band">
      <div class="person">Desmond Kuparik</div>
      <div class="band-mark"></div>
    </div>

    <p class="address">2817 Mellard Rd. Fernwick LV K2p4v8</p>
    <p class="contact">
      <span class="label">P</span> : 613 555 0148
      <span class="label">E:</span> Desmond@kuparik-mail.example
      <span class="label">W:</span> www.7HollowsLL.example
    </p>
  </section>

</body>
</html>
```